Marlow Fenwick Cocktail Menu design

I need a new cocktail menu for our bar 'Marlow Fenwick'.

The logo should read just the full Marlow Fenwick text logo at the top, and the small 'MF' part of the logo in the bottom corners.

The design should be slick, and modern to fit in with our club/bar branding which can be viewed on our social media or website www.marlowfenwick-example.co.uk

```html
<!DOCTYPE html>
<html lang="en">
<head>
<meta charset="utf-8">
<title>Marlow Fenwick – Cocktail Menus</title>
<link href="https://fonts.googleapis.com/css2?family=Roboto:wght@400;500;700;900&display=swap" rel="stylesheet">
<style>
  :root {
    --stage: #e4e4e4;
    --paper: #f4f3ee;
    --ink: #111111;
    --white: #ffffff;
    --accent-red: #e21f26;
    --line-orange: #f2a12a;
    --line-yellow: #f3d21c;
  }
  * { box-sizing: border-box; margin: 0; padding: 0; }
  html, body {
    width: 1200px; height: 1200px; overflow: hidden;
    background: var(--stage);
    font-family: "Roboto", Arial, sans-serif;
    color: var(--ink);
  }
  .canvas { position: relative; width: 1200px; height: 1200px; }

  .menu-page {
    position: absolute;
    width: 477px; height: 672px;
    background: var(--paper);
    overflow: hidden;
  }
  .menu-page--long-islands { left: 84px; top: 150px; }
  .menu-page--classics { left: 617px; top: 358px; }

  .page-lines { position: absolute; inset: 0; width: 100%; height: 100%; }

  .brand { position: absolute; top: 28px; left: 0; right: 0; text-align: center; }
  .brand__name {
    font-weight: 900; font-size: 34px; line-height: 1;
    text-transform: uppercase; letter-spacing: 0;
  }
  .brand__tagline {
    margin-top: 11px; font-weight: 700; font-size: 11px; letter-spacing: 4px;
  }

  .price-badge {
    position: absolute; left: 0; top: 106px;
    width: 136px; height: 40px;
    background: var(--ink); color: var(--white);
    border-radius: 0 6px 6px 0;
    padding: 4px 0 0 29px;
  }
  .price-badge__price { font-weight: 500; font-size: 20px; line-height: 1.05; }
  .price-badge__note { font-weight: 500; font-size: 8.5px; }

  .rule { position: absolute; height: 3px; background: var(--accent-red); }
  .rule--top { left: 150px; width: 174px; top: 125px; }
  .rule--bottom { left: 161px; width: 155px; top: 579px; }

  .menu-title {
    position: absolute; left: 0; right: 0; top: 154px;
    text-align: center; font-weight: 700; font-size: 23px; line-height: 29px;
    text-transform: uppercase;
  }
  .menu-title--single { top: 156px; }
  .menu-title .lower { text-transform: none; }

  .drink-list { position: absolute; left: 0; right: 0; list-style: none; text-align: center; }
  .menu-page--long-islands .drink-list { top: 234px; }
  .menu-page--classics .drink-list { top: 206px; }
  .drink { height: 55px; }
  .drink__name { font-weight: 500; font-size: 16px; line-height: 18px; text-transform: uppercase; }
  .drink__spec { font-size: 9.5px; line-height: 12px; text-transform: uppercase; }

  .page-footer { position: absolute; left: 90px; width: 316px; top: 602px; text-align: center; }
  .page-footer__address { font-size: 10px; }
  .page-footer__web {
    display: inline-block; margin-top: 8px;
    background: var(--ink); color: var(--white);
    font-weight: 700; font-size: 9px; padding: 7px 10px;
    text-transform: uppercase;
  }
  .corner-mark {
    position: absolute; left: 398px; top: 598px;
    font-weight: 900; font-size: 42px; line-height: 1;
  }
</style>
</head>
<body>
<main class="canvas">

  <section class="menu-page menu-page--long-islands">
    <svg class="page-lines" viewBox="0 0 477 672" aria-hidden="true">
      <line x1="390" y1="0" x2="477" y2="354" stroke="var(--line-orange)" stroke-width="0.8"/>
      <line x1="432" y1="0" x2="477" y2="514" stroke="var(--line-yellow)" stroke-width="0.8"/>
      <line x1="0" y1="630" x2="116" y2="558" stroke="var(--line-orange)" stroke-width="0.8"/>
      <line x1="0" y1="584" x2="164" y2="672" stroke="var(--line-yellow)" stroke-width="0.8"/>
    </svg>
    <header class="brand">
      <div class="brand__name">Marlow Fenwick</div>
      <div class="brand__tagline">BAR . CLUB . FOOD</div>
    </header>
    <div class="price-badge">
      <div class="price-badge__price">ALL £4.95</div>
      <div class="price-badge__note">DURING HAPPY HOUR</div>
    </div>
    <div class="rule rule--top"></div>
    <h2 class="menu-title"><span class="lower">MF’s</span> Long List of<br>‘Long Islands’</h2>
    <ul class="drink-list">
      <li class="drink"><div class="drink__name">Long Island Iced Tea — £9.50</div><div class="drink__spec">Vodka, gin, rum, tequila, orange liqueur, lemon &amp; cola</div></li>
      <li class="drink"><div class="drink__name">Long Beach Iced Tea — £9.50</div><div class="drink__spec">Vodka, gin, rum, tequila, orange liqueur, lemon &amp; cranberry</div></li>
      <li class="drink"><div class="drink__name">AMF — £9.50</div><div class="drink__spec">Vodka, gin, rum, tequila, blue curacao, lemon &amp; lemonade</div></li>
      <li class="drink"><div class="drink__name">Tokyo Iced Tea — £9.50</div><div class="drink__spec">Vodka, gin, rum, tequila, melon liqueur, lemon &amp; lemonade</div></li>
      <li class="drink"><div class="drink__name">Tiki Iced Tea — £9.50</div><div class="drink__spec">Vodka, gin, coconut rum, tequila, orange liqueur, lime &amp; pineapple</div></li>
      <li class="drink"><div class="drink__name">Long Island Iced Coffee — £9.50</div><div class="drink__spec">Vodka, gin, rum, tequila, Irish cream, milk, salted caramel syrup &amp; espresso</div></li>
    </ul>
    <div class="rule rule--bottom"></div>
    <footer class="page-footer">
      <div class="page-footer__address">Marlow Fenwick, 42 Tanner Lane, Manchester, M1 4XQ</div>
      <div class="page-footer__web">marlowfenwick-example.co.uk</div>
    </footer>
    <div class="corner-mark">MF</div>
  </section>

  <section class="menu-page menu-page--classics">
    <svg class="page-lines" viewBox="0 0 477 672" aria-hidden="true">
      <line x1="390" y1="0" x2="477" y2="354" stroke="var(--line-orange)" stroke-width="0.8"/>
      <line x1="432" y1="0" x2="477" y2="514" stroke="var(--line-yellow)" stroke-width="0.8"/>
      <line x1="0" y1="630" x2="116" y2="558" stroke="var(--line-orange)" stroke-width="0.8"/>
      <line x1="0" y1="584" x2="164" y2="672" stroke="var(--line-yellow)" stroke-width="0.8"/>
    </svg>
    <header class="brand">
      <div class="brand__name">Marlow Fenwick</div>
      <div class="brand__tagline">BAR . CLUB . FOOD</div>
    </header>
    <div class="price-badge">
      <div class="price-badge__price">ALL £4.95</div>
      <div class="price-badge__note">DURING HAPPY HOUR</div>
    </div>
    <div class="rule rule--top"></div>
    <h2 class="menu-title menu-title--single">Classic Cocktails</h2>
    <ul class="drink-list">
      <li class="drink"><div class="drink__name">Bitter Spritz — £8.50</div><div class="drink__spec">Bitter aperitivo, prosecco &amp; soda</div></li>
      <li class="drink"><div class="drink__name">Margarita – £7.95</div><div class="drink__spec">Tequila, orange liqueur &amp; lime</div></li>
      <li class="drink"><div class="drink__name">Pornstar Martini — £8.50</div><div class="drink__spec">Vanilla vodka, passion fruit liqueur, passion fruit puree, pineapple &amp; lime</div></li>
      <li class="drink"><div class="drink__name">Espresso Martini — £8.50</div><div class="drink__spec">Vanilla vodka, coffee liqueur &amp; espresso</div></li>
      <li class="drink"><div class="drink__name">Gin Spritz — £7.95</div><div class="drink__spec">Pink gin, strawberry syrup, prosecco &amp; lemonade</div></li>
      <li class="drink"><div class="drink__name">Mai Tai — £8.95</div><div class="drink__spec">Dark rum, white rum, orange liqueur, orgeat, lime &amp; pineapple</div></li>
      <li class="drink"><div class="drink__name">Whiskey Sour — £8.95</div><div class="drink__spec">Bourbon whiskey, lemon &amp; egg white</div></li>
    </ul>
    <div class="rule rule--bottom"></div>
    <footer class="page-footer">
      <div class="page-footer__address">Marlow Fenwick, 42 Tanner Lane, Manchester, M1 4XQ</div>
      <div class="page-footer__web">marlowfenwick-example.co.uk</div>
    </footer>
    <div class="corner-mark">MF</div>
  </section>

</main>
</body>
</html>
```